Financial Advisor Resource Firm needs business card design

Need business card design for company in Omaha NE called Tallowbrook Partners. We provide resources to financial advisors....workshop programs, retirement analysis, and insurance planning. I would like to see designs that use grays, greens, black, and white colors. The final design should communicate 'collaboration' and be simple yet attractive to financial planning clients. I will attached our logo and another picture of a puzzle piece coming together. I would like the incorporate the puzzle picture somehow, maybe on the back somehow, with color or just the gray scale....OR, the picture be the front of the card with 'Tallowbrook' definition on it (see upload) and then company logo, employee name, title, address on the back (see ppt uploaded). The following disclosure needs to be included somewhere- Advisory services offered through Marlowe Ridge Advisors, LLC.
Updates

I uploaded a svg and ai file of the logo

Target Market(s)

Financial planning clients and financial advisors....so pretty diverse age range of about 40-70.

Industry/Entity Type

Financial Planning

Contact Information for Business Card

Dennis K. Holloway, MBA
Founder/President
5727 E. Larkspur Avenue
Suite 418
Omaha, NE 68297
Phone- (402) 555-0147
Cell- (402) 555-0183
Fax- (402) 555-0129
email- dennis@tallowbrookgroup.example
web address- www.tallowbrookgroup.example

Colors
1b1b1b
474747
d3d3d3
ffffff
9bcb3c
abd036

Requirements
Must have
• Must include logo provided, must be 2 sided, and must have disclosure...all of these items listed in project description

```html
<!DOCTYPE html>
<html lang="en">
<head>
<meta charset="utf-8">
<title>Tallowbrook Partners – Business Card</title>
<link href="https://fonts.googleapis.com/css2?family=Questrial&display=swap" rel="stylesheet">
<style>
  :root {
    --ink: #1b1b1b;
    --charcoal: #474747;
    --mist: #d3d3d3;
    --paper: #ffffff;
    --leaf: #9bcb3c;
    --lime: #abd036;
    --backdrop: #ececec;
  }
  * { box-sizing: border-box; margin: 0; padding: 0; }
  html, body { width: 1200px; height: 900px; overflow: hidden; }
  body {
    background: var(--backdrop);
    font-family: "Questrial", "Century Gothic", sans-serif;
    position: relative;
  }
  .card {
    position: absolute;
    width: 560px;
    height: 320px;
    border-radius: 4px;
    overflow: hidden;
    box-shadow: 0 6px 18px rgba(0,0,0,0.18);
  }
  .brand {
    display: flex;
    align-items: center;
    gap: 12px;
    color: var(--ink);
    white-space: nowrap;
  }
  .brand-mark {
    flex: none;
    border-radius: 50%;
    background: var(--leaf);
  }
  /* Back side */
  .card-back {
    left: 70px; top: 80px;
    background: var(--charcoal);
  }
  .card-back .brand {
    position: absolute;
    left: 0; right: 0; top: 108px;
    justify-content: center;
    font-size: 42px;
    letter-spacing: 1px;
  }
  .card-back .brand-mark { width: 34px; height: 34px; }
  .card-back .web {
    position: absolute;
    left: 0; right: 0; top: 186px;
    text-align: center;
    font-size: 19px;
    letter-spacing: 4px;
    color: var(--ink);
  }
  /* Front side */
  .card-front {
    left: 570px; top: 500px;
    background: var(--charcoal);
  }
  .front-top {
    position: absolute;
    left: 0; top: 0; width: 100%; height: 140px;
    background: var(--mist);
  }
  .front-top .brand {
    position: absolute;
    left: 30px; top: 20px;
    font-size: 32px;
  }
  .front-top .brand-mark { width: 26px; height: 26px; }
  .front-top .person {
    position: absolute;
    left: 30px; top: 74px;
    font-size: 23px;
    color: var(--ink);
  }
  .front-top .role {
    position: absolute;
    left: 30px; top: 106px;
    font-size: 16px;
    letter-spacing: 3px;
    color: var(--charcoal);
  }
  .contact {
    position: absolute;
    left: 30px; top: 150px;
    color: var(--leaf);
    font-size: 17px;
    line-height: 23px;
    letter-spacing: 1px;
    list-style: none;
  }
  .contact .address { display: flex; gap: 8px; }
  .contact .pin { width: 14px; height: 20px; margin-top: 1px; flex: none; }
  .disclosure {
    position: absolute;
    left: 30px; right: 30px; top: 296px;
    font-size: 11px;
    letter-spacing: 0.5px;
    color: var(--mist);
  }
</style>
</head>
<body>
  <section class="card card-back" aria-label="Card back">
    <div class="brand"><span class="brand-mark" aria-hidden="true"></span>Tallowbrook Partners</div>
    <div class="web">www.tallowbrookgroup.example</div>
  </section>

  <section class="card card-front" aria-label="Card front">
    <div class="front-top">
      <div class="brand"><span class="brand-mark" aria-hidden="true"></span>Tallowbrook Partners</div>
      <div class="person">Dennis K. Holloway, MBA</div>
      <div class="role">Founder/President</div>
    </div>
    <ul class="contact">
      <li class="address">
        <svg class="pin" viewBox="0 0 14 20" aria-hidden="true">
          <path d="M7 0C3.1 0 0 3.1 0 7c0 5 7 13 7 13s7-8 7-13c0-3.9-3.1-7-7-7zm0 10a3 3 0 1 1 0-6 3 3 0 0 1 0 6z" fill="var(--leaf)"/>
        </svg>
        <span>5727 E. Larkspur Avenue, Suite 418<br>Omaha, NE 68297</span>
      </li>
      <li>P: (402) 555-0147</li>
      <li>C: (402) 555-0183</li>
      <li>F: (402) 555-0129</li>
      <li>E-mail: dennis@tallowbrookgroup.example</li>
    </ul>
    <p class="disclosure">Advisory services offered through Marlowe Ridge Advisors, LLC</p>
  </section>
</body>
</html>
```